Large online photo magazine needs redesign

We have previously digitised a historical photographic magazine of around 20,000 printed pages and made it available online. The magazine ran up to the early 1970s, and the content is largely black and white photographs of local events, accompanied by short captions.

Although the content is very rich, the design needs to be revisited so that:
* it is visually appealing
* it is responsive (i.e. works in browsers across all manner of devices)
* is faithful to the nature of the content

There are only a few core page types, and the central one is the article page, an example of which can be seen at:
http://tawaleaf.org.nz/gisborne/issue/KMW73_19600714/t1-body-d4.html

Any design submitted should be based on the treatment of an article page such as the above.

Given the large number of pages on our site, we need a design which can be templated to work for any content in the collection, i.e. we cannot hand-craft our templates to match a given page of content, rather a template must work acceptably well for all content.

The current site, although basic in design, has the advantage that it is quite efficient in the amount of data per page request (around 100k - 200k). While not adverse to web fonts, banner imagery etc, we will carefully consider the benefit gained from any such treatment against the amount of extra data that needs to be downloaded to the client's browser.

For the right design, we are able ourselves to adapt it to a CSS layout.

An example of each core page type is as follows (though for this project we only expect a design for a single page, as itemised above):

http://tawaleaf.org.nz/gisborne/index.html
http://tawaleaf.org.nz/gisborne/about.html
http://tawaleaf.org.nz/gisborne/help.html
http://tawaleaf.org.nz/gisborne/initial/index.html
http://tawaleaf.org.nz/gisborne/search/results?type=section&text=smith&cmdSubmit=Go
http://tawaleaf.org.nz/gisborne/advanced-search/index.html
http://tawaleaf.org.nz/gisborne/issue/KMW73_19600714/t1-front-d1.html
http://tawaleaf.org.nz/gisborne/issue/KMW73_19600714/index.html
http://tawaleaf.org.nz/gisborne/issue/KMW73_19600714/fig-KMW73_19600714_005a.html
http://tawaleaf.org.nz/gisborne/issue/KMW73_19600714/KMW73_19600714_012.html
http://tawaleaf.org.nz/gisborne/issue/KMW73_19600714/thumbnails.html

Reason: Extending the deadline by three days as a number of designers have only recently accepted the invitation.

A general browsing audience of all ages, but skewed towards the older generations, and those interested in family / regional history.

The average user will not be particularly web-savy, and the treatment of the content should not detract / distract from the actual content itself.

Events

• * it is visually appealing
The content should be visually appealing to the audience, which can be defined as a general browsing audience of all ages, but skewed towards the middle and older generations.

* it is responsive (the design can be adapted - by us - to work in browsers across all manner of devices)

The magazine covers (http://tawaleaf.org.nz/gisborne/issues/index.html) offer some possible inspiration for treatment of the material.

```html
<!DOCTYPE html>
<html lang="en">
<head>
<meta charset="utf-8">
<title>Indoor Basketball – Tawa Leaf News</title>
<link href="https://fonts.googleapis.com/css2?family=Noto+Sans:wght@400;700&display=swap" rel="stylesheet">
<style>
:root{
  --maroon:#340a18;
  --rose:#c93c53;
  --ink:#111111;
  --white:#ffffff;
  --photo-dark:#2b3329;
  --photo-mid:#7d8676;
  --paper:#f3ecd2;
}
*{box-sizing:border-box;margin:0;padding:0}
html,body{width:1200px;height:1034px;overflow:hidden;background:var(--white);font-family:"Noto Sans",Verdana,sans-serif;color:var(--ink)}
a{color:inherit;text-decoration:none}
.utility-bar{position:absolute;left:0;top:0;width:1200px;height:35px;background:var(--maroon)}
.utility-links{position:absolute;left:169px;top:11px;font-size:10px;color:var(--white)}
.utility-links span{margin:0 3px}
.search{position:absolute;left:843px;top:7px;display:flex;gap:4px}
.search-field{width:154px;height:19px;background:var(--white);border-radius:9px 0 0 9px}
.search-button{width:28px;height:19px;background:var(--white);border-radius:0 9px 9px 0;display:flex;align-items:center;justify-content:center}
.masthead{position:absolute;left:0;top:35px;width:1200px;height:92px;background:var(--rose)}
.brand{position:absolute;left:168px;top:22px;font-size:36px;font-weight:700;color:var(--white);letter-spacing:1px}
.main-nav{position:absolute;left:643px;top:24px;display:flex;gap:9px;font-size:12.5px;color:var(--white);text-transform:uppercase}
.breadcrumb{position:absolute;left:170px;top:134px;font-size:9.5px}
.issue-title{position:absolute;left:172px;top:163px;font-size:17px;font-weight:700;color:var(--rose);letter-spacing:.5px}
.print-link{position:absolute;left:935px;top:163px;display:flex;align-items:center;gap:6px;font-size:9.5px}
.issue-rule{position:absolute;left:166px;top:188px;width:868px;height:11px;background:var(--rose)}
.page-panel{position:absolute;left:167px;top:219px;width:275px;height:211px;background:var(--maroon)}
.page-thumb{position:absolute;left:22px;top:15px;width:231px;height:146px;background:linear-gradient(135deg,var(--paper),#c9c3a8);padding:4px;display:grid;grid-template-columns:1fr 1fr;gap:3px}
.page-thumb div{background:linear-gradient(160deg,var(--photo-mid),var(--photo-dark))}
.view-page{position:absolute;left:22px;top:171px;font-size:17px;font-weight:700;color:var(--white);text-decoration:underline}
.article-title{position:absolute;left:463px;top:213px;font-size:17px;font-weight:700;color:var(--rose);letter-spacing:.5px}
.photo{position:absolute;background:radial-gradient(ellipse at 50% 40%,var(--photo-mid),var(--photo-dark))}
.caption{position:absolute;left:689px;width:344px;font-size:13.5px;line-height:15.7px}
.article-nav{position:absolute;left:166px;top:901px;width:868px;height:40px;background:var(--rose);color:var(--white);font-size:12.5px}
.article-nav a{position:absolute;top:13px;display:flex;align-items:center;gap:7px}
.footer{position:absolute;left:170px;top:973px;display:flex;align-items:center;gap:14px;font-size:9.5px}
.licence-badge{width:81px;height:28px;background:var(--ink);border:2px solid #9b9b9b}
</style>
</head>
<body>
<header>
  <div class="utility-bar">
    <nav class="utility-links"><a href="#">Advanced search</a><span>|</span><a href="#">Help</a><span>|</span><a href="#">Report an error</a></nav>
    <div class="search">
      <div class="search-field"></div>
      <div class="search-button"><svg width="18" height="14" viewBox="0 0 18 14"><circle cx="6" cy="6" r="4.2" fill="none" stroke="#c93c53" stroke-width="1.8"/><line x1="9" y1="9" x2="16" y2="12.5" stroke="#c93c53" stroke-width="2.4" stroke-linecap="round"/></svg></div>
    </div>
  </div>
  <div class="masthead">
    <a class="brand" href="#">Tawa Leaf News</a>
    <nav class="main-nav"><a href="#">Home</a><a href="#">About</a><a href="#">Browse Tawa Leaf News</a><a href="#">A-Z People</a></nav>
  </div>
</header>

<main>
  <div class="breadcrumb">Tawa Leaf News &gt; Issues &gt; KMW01_19540603 &gt; t1-body-d7</div>
  <h1 class="issue-title">NO 1 JUNE 3, 1954</h1>
  <a class="print-link" href="#">Print this article
    <svg width="19" height="22" viewBox="0 0 19 22"><path d="M4 1h10l4 4v16H4z" fill="none" stroke="#111" stroke-width="1.6"/><path d="M1 6v15h3" fill="none" stroke="#111" stroke-width="1.4"/><line x1="8" y1="10" x2="14" y2="10" stroke="#111" stroke-width="1.4"/><line x1="8" y1="13" x2="14" y2="13" stroke="#111" stroke-width="1.4"/><line x1="8" y1="16" x2="12" y2="16" stroke="#111" stroke-width="1.4"/></svg>
  </a>
  <div class="issue-rule"></div>

  <aside class="page-panel">
    <div class="page-thumb" role="img" aria-label="Thumbnail of the printed magazine page with basketball and landscape photographs">
      <div></div><div></div><div></div><div></div>
    </div>
    <a class="view-page" href="#">VIEW PAGE</a>
  </aside>

  <article>
    <h2 class="article-title">INDOOR BASKETBALL</h2>
    <div class="photo" style="left:463px;top:251px;width:201px;height:160px" role="img" aria-label="Women's basketball players leaping for the ball, with printed caption below"></div>
    <p class="caption" style="top:248px">Action in indoor basketball is so rapid that when the high-speed camera "freezes" the contortions of players straining to score a goal, some strange poses are revealed. These "shots" were taken in the Army Hall on a recent Wednesday night. Above, Kea (white) plays Rovers.</p>
    <div class="photo" style="left:464px;top:432px;width:201px;height:215px" role="img" aria-label="Two men's basketball players jumping beneath the hoop"></div>
    <p class="caption" style="top:427px">An incident in the men's game, Comets v. Hawks.</p>
    <div class="photo" style="left:464px;top:674px;width:207px;height:195px" role="img" aria-label="Men's basketball players contesting near the basket"></div>
    <p class="caption" style="top:671px">Meteors and Aces in action near the basket. Tawa Bay has thriving indoor basketball competition, is fortunate in having such a large hall available. Tour­nament which attracts teams from all over North Island is to be held here during Queen's Birthday weekend.</p>
  </article>

  <nav class="article-nav">
    <a href="#" style="left:12px"><svg width="20" height="18" viewBox="0 0 20 18"><path d="M10 0 1 9l9 9zM19 0l-9 9 9 9z" fill="#fff"/></svg>PREVIOUS ARTICLE</a>
    <a href="#" style="left:172px">NEXT ARTICLE<svg width="20" height="18" viewBox="0 0 20 18"><path d="M1 0l9 9-9 9zM10 0l9 9-9 9z" fill="#fff"/></svg></a>
    <a href="#" style="left:716px;top:12px">ISSUE CONTENTS<svg width="23" height="17" viewBox="0 0 23 17"><rect y="0" width="23" height="4" rx="2" fill="#fff"/><rect y="6.5" width="23" height="4" rx="2" fill="#fff"/><rect y="13" width="23" height="4" rx="2" fill="#fff"/></svg></a>
  </nav>
</main>

<footer class="footer">
  <div class="licence-badge" role="img" aria-label="Licence badge"></div>
  <span>© 2012 Harbourside Memorial Library</span>
</footer>
</body>
</html>
```